Brightwire Hollow Business cards

one side I would like my logo (uploaded) and the other side I want my details. I'm an electrician in sydney. The logo side I'm happy with just a white background and our logo in the middle.

Details for other side
24/7 Sydney Electrician
Marcus Pell
0431 587 219
marcus@brightwirehollow.com.au
brightwirehollow.com.au
icons for facebook, instagram, linked in

Industry/Entity Type

electrician

Contact Information for Business Card

company info

```html
<!DOCTYPE html>
<html lang="en">
<head>
<meta charset="utf-8">
<title>Brightwire Hollow – Business Cards</title>
<link rel="stylesheet" href="https://fonts.googleapis.com/css2?family=Lato:ital,wght@0,400;0,700;0,900;1,400;1,700;1,900&display=swap">
<style>
  :root {
    --backdrop: #3b3c3f;
    --card-white: #ffffff;
    --brand-red: #e42313;
    --ink-black: #1c1a1b;
    --text-light: #ffffff;
    --text-dark: #1c1a1b;
  }
  * { margin: 0; padding: 0; box-sizing: border-box; }
  html, body {
    width: 1200px;
    height: 1200px;
    overflow: hidden;
    background: var(--backdrop);
    font-family: "Lato", sans-serif;
  }
  .canvas { position: relative; width: 1200px; height: 1200px; }

  .card {
    position: absolute;
    left: 162px;
    width: 878px;
    height: 513px;
    background: var(--card-white);
    overflow: hidden;
  }
  .card--details { top: 61px; }
  .card--logo { top: 626px; }

  .card__shapes { position: absolute; inset: 0; width: 878px; height: 513px; }
  .shape--red { fill: var(--brand-red); }
  .shape--black { fill: var(--ink-black); }

  .wordmark {
    font-weight: 900;
    color: var(--brand-red);
    letter-spacing: 0.5px;
    white-space: nowrap;
    line-height: 1;
  }
  .card--details .wordmark {
    position: absolute;
    left: 66px;
    top: 100px;
    font-size: 46px;
  }
  .card--logo .wordmark {
    position: absolute;
    left: 0;
    right: 0;
    top: 226px;
    text-align: center;
    font-size: 62px;
  }

  .tagline {
    position: absolute;
    left: 66px;
    top: 340px;
    font-size: 22px;
    font-style: italic;
    color: var(--text-dark);
  }

  .social-links {
    position: absolute;
    left: 64px;
    top: 410px;
    display: flex;
    gap: 14px;
  }
  .social-links span {
    width: 24px;
    height: 24px;
    border-radius: 50%;
    background: var(--text-light);
  }

  .holder-name {
    position: absolute;
    right: 70px;
    top: 270px;
    font-size: 37px;
    font-weight: 900;
    font-style: italic;
    color: var(--text-light);
    text-transform: uppercase;
    letter-spacing: -0.5px;
  }

  .contact-list {
    position: absolute;
    right: 62px;
    top: 355px;
    list-style: none;
  }
  .contact-list li {
    display: flex;
    align-items: center;
    justify-content: flex-end;
    height: 34.5px;
    font-size: 21px;
    color: var(--text-light);
  }
  .contact-list svg {
    width: 18px;
    height: 18px;
    margin-left: 20px;
    fill: none;
    stroke: var(--brand-red);
    stroke-width: 2;
  }
  .contact-list svg .solid { fill: var(--brand-red); stroke: none; }
</style>
</head>
<body>
<main class="canvas">

  <section class="card card--details" aria-label="Business card, details side">
    <svg class="card__shapes" viewBox="0 0 878 513" aria-hidden="true">
      <polygon class="shape--red" points="700,126 878,126 878,160 673,160"/>
      <polygon class="shape--black" points="594,161 878,161 878,513 0,513 0,469 348,469"/>
      <polygon class="shape--red" points="0,398 362,398 338,446 0,446"/>
    </svg>

    <div class="wordmark">Brightwire Hollow</div>

    <p class="tagline">24/7 Sydney Electrician</p>

    <div class="social-links" aria-label="Social media">
      <span></span><span></span><span></span>
    </div>

    <h1 class="holder-name">Marcus Pell</h1>

    <ul class="contact-list">
      <li>0431 587 219
        <svg viewBox="0 0 18 18" aria-hidden="true"><rect x="5" y="1.5" width="8" height="15" rx="1.5"/><circle class="solid" cx="9" cy="13.5" r="1"/></svg>
      </li>
      <li>marcus@brightwirehollow.com.au
        <svg viewBox="0 0 18 18" aria-hidden="true"><rect class="solid" x="2" y="4" width="14" height="10" rx="1"/><polyline points="2.5,4.5 9,10 15.5,4.5" stroke="#1c1a1b" stroke-width="1.5"/></svg>
      </li>
      <li>brightwirehollow.com.au
        <svg viewBox="0 0 18 18" aria-hidden="true"><circle cx="9" cy="9" r="6.5"/><line x1="2.5" y1="9" x2="15.5" y2="9" stroke-width="1.3"/><ellipse cx="9" cy="9" rx="2.8" ry="6.5" stroke-width="1.3"/></svg>
      </li>
    </ul>
  </section>

  <section class="card card--logo" aria-label="Business card, logo side">
    <div class="wordmark">Brightwire Hollow</div>
  </section>

</main>
</body>
</html>
```